Merrivale construction website for a high end luxury custom home builder

I need a website designed for a high end luxury custom home builder. I would like the website to host a number activities. A blog/vlog on the page where I can post about the projects being built how to's what to look out for during the build, A designated testimonial page but also having testimonials posted on the other pages like the gallery linked to the photos of the completed projects. a gallery page, an about us page, services page that demonstrate what we do and what we are capable of, and hopefully when I start winning awards, and awards page.
Home page
about us page
services page
gallery
testimonial
awards page but I my need to add that later.
I already have the domain name for the website. www.merrivaleconstruction.com.au
I recently completed a sketch hive page for my logo and will post the logo documents below.

Target Market(s)

I'd like to target professions with cash enough to build a house. I would like peolpe to understand that they are buy a price when they are getting quote to build there house. It seems like people just look for the cheapest price and end up with an inferior product. Where as people need to understand that a builder with the high price ( not astronomically higher 15-20% higher) are the ones with correct systems in place, a bide by correct OHS and use proper and correct product. If that can be conveyed through the website somehow, without saying it directly, it would be awesome.

Font styles to use
Sans Serif

Requirements
Must have
• I would like the testimonials to have a designated page (mentioned in the brief) but I would like the testimonials to be linked to the gallery page and when the picture are open of completed job the relevant testimonials would pop up near the pictures.

Nice to have
• I would like peolpe to understand that they are buy a price when they are getting quote to build there house. It seems like people just look for the cheapest price and end up with an inferior product. Where as people need to understand that a builder with the high price ( not astronomically higher 15-20% higher) are the ones with correct systems in place, a bide by correct OHS and use proper and correct product. If that can be conveyed through the website somehow, without saying it directly, it would be awesome.

```html
<!DOCTYPE html>
<html lang="en">
<head>
<meta charset="utf-8">
<title>Merrivale Construction — Luxury Is Personal</title>
<link rel="stylesheet" href="https://fonts.googleapis.com/css2?family=Playfair+Display:wght@400;700&family=Roboto:wght@400;500&display=swap">
<style>
:root{
  --ink:#1d1d24;
  --text:#444;
  --muted:#8a8a8a;
  --purple:#4a2fbd;
  --gold:#c9a46c;
  --navy:#0f1b2f;
  --pale:#f5f6f5;
  --line:#ececec;
  --white:#fff;
}
*{margin:0;padding:0;box-sizing:border-box}
html,body{width:1200px;height:3774px;overflow:hidden;background:var(--white)}
body{position:relative;font-family:"Roboto",sans-serif;color:var(--text);font-size:10px}
.abs{position:absolute}
.serif{font-family:"Playfair Display",serif}
.frame{position:absolute;left:142px;width:917px}

/* header */
.brand{left:217px;top:16px;display:flex;align-items:center;gap:8px}
.brand-mark{width:26px;height:26px;border:3px solid #2d6fb7;border-radius:50%}
.brand-name{font-family:"Playfair Display",serif;font-weight:700;font-size:17px;color:#2d6fb7;line-height:1}
.brand-name small{display:block;font-size:7px;letter-spacing:2.4px;font-weight:700;text-transform:uppercase}
.contact{top:18px;display:flex;gap:8px;font-size:9.5px;color:var(--ink);line-height:15px}
.contact svg{margin-top:2px}
.rule{height:1px;background:var(--line)}
.nav{left:253px;top:80px;display:flex;gap:31px;font-family:"Playfair Display",serif;font-size:9.5px;text-transform:uppercase;color:var(--ink)}
.nav .active{color:var(--purple)}
.social-top{left:867px;top:82px;display:flex;gap:9px}
.social-top i{width:6px;height:6px;background:#b5b5b5;border-radius:50%;display:block}

/* hero */
.hero{top:108px;height:498px;background:linear-gradient(180deg,#3c3f3d 0%,#3e4f4a 35%,#24505c 60%,#1c4c66 100%)}
.hero-shade{position:absolute;inset:0;background:rgba(20,25,40,.35)}
.hero-kicker{top:266px;left:0;width:1200px;text-align:center;font-family:"Playfair Display",serif;font-weight:700;font-size:10.5px;color:#fff;letter-spacing:.3px}
.hero-title{top:290px;left:0;width:1200px;text-align:center;font-family:"Playfair Display",serif;font-size:45px;color:#fff;letter-spacing:.5px}
.search-panel{left:297px;top:542px;width:607px;height:81px;background:#fff;box-shadow:0 6px 20px rgba(0,0,0,.08)}
.search-input{left:318px;top:567px;width:275px;height:29px;border:1px solid #e3e3e3;font-size:8px;color:#999;padding:9px 12px}

/* welcome */
.photo{position:absolute}
.welcome h2{font-family:"Playfair Display",serif;font-weight:700;font-size:27px;line-height:32px;color:var(--ink)}
.welcome p{font-size:9.5px;line-height:15.5px;color:#333;margin-top:12px;width:360px}
.btn{display:inline-block;background:var(--purple);color:#fff;font-family:"Playfair Display",serif;font-weight:700;font-size:9px;text-transform:uppercase;padding:11px 21px;margin-top:26px}

/* section heads */
.sec-icon{left:578px;width:44px}
.sec-title{left:0;width:1200px;text-align:center;font-family:"Playfair Display",serif;font-weight:700;font-size:26px;color:var(--ink)}

/* cards */
.card{position:absolute;width:219px;background:#fff;box-shadow:0 4px 18px rgba(0,0,0,.07)}
.card .pic{height:208px;clip-path:polygon(0 0,100% 0,100% 93%,0 100%)}
.card p{font-size:9.5px;line-height:15.5px;color:#222;padding:8px 24px 0 25px}

/* video band */
.band{top:1606px;height:353px;background:linear-gradient(120deg,#5a5a58 0%,#6f6762 35%,#3a3230 55%,#5d5a63 80%,#716d77 100%)}
.play{left:575px;top:1723px;width:50px;height:50px;border-radius:50%;background:#fff;display:flex;align-items:center;justify-content:center}
.band-title{top:1786px;left:0;width:1200px;text-align:center;font-family:"Playfair Display",serif;font-weight:700;font-size:31px;color:#fff}
.band-sub{top:1837px;left:0;width:1200px;text-align:center;font-size:9.5px;color:#fff}

/* facilities */
.facilities{top:1959px;height:429px;background:var(--pale)}
.fac{position:absolute;top:2177px;width:219px;height:129px;background:#fff;padding:20px 22px}
.fac h3{display:flex;align-items:center;gap:7px;font-family:"Playfair Display",serif;font-weight:400;font-size:15px;color:var(--ink)}
.fac p{font-size:9.5px;line-height:15.5px;color:#333;margin-top:6px}

/* testimonials */
.quote-track{left:253px;top:2581px;width:693px;height:147px;overflow:hidden}
.quote{position:absolute;top:0;width:218px;height:147px;background:var(--pale);padding:20px 16px 0 21px;display:flex;gap:12px}
.avatar{flex:none;width:42px;height:42px;border-radius:50%;background:radial-gradient(circle at 50% 40%,#8a8076,#3b3a3c)}
.quote p{font-size:9.5px;line-height:15.5px;color:#222}
.quote h4{font-family:"Playfair Display",serif;font-weight:400;font-size:15px;color:var(--ink);margin-top:8px}
.quote span{font-size:8px;color:var(--muted)}
.dots{left:582px;top:2771px;display:flex;gap:9px}
.dots i{width:6px;height:6px;border-radius:50%;background:#cfcfcf;display:block}
.dots i.on{background:var(--purple)}

/* news */
.news .pic{height:224px;clip-path:polygon(0 0,100% 0,100% 86%,0 100%)}
.news h3{font-family:"Playfair Display",serif;font-weight:700;font-size:15px;color:var(--ink);padding:10px 25px 0}
.meta{display:flex;gap:14px;font-size:8px;color:var(--muted);padding:10px 25px 0}
.meta b{font-weight:400;color:var(--gold)}
.news p{padding-top:8px}

/* footer */
.footer{top:3437px;height:337px;background:var(--navy)}
.fcol{position:absolute;top:3513px}
.fcol h5{font-family:"Playfair Display",serif;font-weight:700;font-size:14.5px;color:#fff;margin-bottom:12px}
.fcol a{display:block;font-size:9px;color:#9aa2b2;line-height:22px;text-decoration:none}
.fcol .note{font-size:9px;color:#9aa2b2;line-height:15px}
.sub{display:flex;margin-top:16px}
.sub .field{width:114px;height:23px;background:#27324a;font-size:8px;color:#8a93a6;padding:7px 7px}
.sub .go{width:72px;height:23px;background:var(--gold);font-family:"Playfair Display",serif;font-weight:700;font-size:7.5px;color:#fff;text-transform:uppercase;display:flex;align-items:center;justify-content:center}
.copy{left:253px;top:3681px;font-size:9px;color:#fff}
.copy em{font-style:normal;color:var(--gold)}
.fsocial{left:854px;top:3677px;display:flex;gap:5px}
.fsocial i{width:19px;height:19px;background:#2a3550;display:block}
</style>
</head>
<body>

<!-- header -->
<div class="abs brand"><span class="brand-mark"></span><span class="brand-name">Merrivale<small>construction</small></span></div>

<div class="abs contact" style="left:713px">
  <svg width="11" height="11" viewBox="0 0 24 24"><path d="M6 2l4 4-2.5 2.5a14 14 0 006 6L16 12l4 4-3 3C9 19 5 15 3 5z" fill="none" stroke="#4a2fbd" stroke-width="2"/></svg>
  <div>Have any question?<br>Free: +12 480 7716</div>
</div>
<div class="abs contact" style="left:845px">
  <svg width="13" height="10" viewBox="0 0 26 20"><rect x="1" y="1" width="24" height="18" fill="none" stroke="#4a2fbd" stroke-width="2"/><path d="M1 1l12 10L25 1" fill="none" stroke="#4a2fbd" stroke-width="2"/></svg>
  <div>Have any question?<br>Free: +12 480 7716</div>
</div>

<div class="frame rule" style="top:64px"></div>
<nav class="abs nav">
  <span class="active">Home</span><span>About Us</span><span>Services</span><span>Gallery</span><span>Testimonial</span><span>Contact</span>
</nav>
<div class="abs social-top"><i></i><i></i><i></i><i></i><i></i></div>

<!-- hero -->
<section class="frame hero" role="img" aria-label="Evening view of a resort pool lined with palm trees in front of a tiled-roof villa"><div class="hero-shade"></div></section>
<div class="abs hero-kicker">SEE WHAT A DIFFERENCE A MERRIVALE MAKES</div>
<h1 class="abs hero-title" style="font-weight:400">LUXURY <i style="font-weight:700">IS</i> PERSONAL</h1>
<div class="abs search-panel"></div>
<div class="abs search-input">Enter your keywords...</div>

<!-- welcome -->
<div class="photo" style="left:253px;top:713px;width:160px;height:181px;background:linear-gradient(135deg,#6a5a4c,#b8a48a 55,#4b3f52)" role="img" aria-label="Hotel suite lounge with patterned rug and warm lighting"></div>
<div class="photo" style="left:416px;top:713px;width:113px;height:181px;background:linear-gradient(180deg,#f0f0f2,#d9dde2 70%,#3c78a6)" role="img" aria-label="White bedroom with blue cushion and framed green print"></div>
<div class="photo" style="left:253px;top:897px;width:160px;height:124px;background:linear-gradient(135deg,#3b3f47,#6f7681 60%,#b9bcc0)" role="img" aria-label="Dark living room with wall-mounted television"></div>
<div class="photo" style="left:416px;top:897px;width:113px;height:124px;background:linear-gradient(135deg,#cfd7df,#8e99a4 60%,#5e6670)" role="img" aria-label="Bright lounge with grey sofa and sea view"></div>

<div class="abs welcome" style="left:587px;top:760px">
  <h2>Welcome<br>to our Projects</h2>
  <p>Beginning blessed second a creepeth. Darkness wherein fish years good air whose after seed appear midst evenin, appear void give third bearing divide one so blessed moved firmament gathered</p>
  <p>Beginning blessed second a creepeth. Darkness wherein fish years good air whose after seed appear midst evenin, appear void give third bearing divide one so blessed</p>
  <span class="btn">Learn More</span>
</div>

<!-- explore projects -->
<svg class="abs sec-icon" style="top:1105px" height="22" viewBox="0 0 44 22"><path d="M4 9h36v8H4zM8 9V3h28v6M6 17v4M38 17v4" fill="none" stroke="#c9a46c" stroke-width="1.6"/></svg>
<h2 class="abs sec-title" style="top:1134px">Explore Our Projects</h2>

<div class="card" style="left:253px;top:1222px;height:291px">
  <div class="pic" style="background:linear-gradient(180deg,#9aa8bc 0%,#8d6a4f 40%,#4f7e99 75%,#7aa6bd)" role="img" aria-label="Bedroom with carved headboard, bedside lamps and blue quilt"></div>
  <p>Beginning fourth dominion creeping god was. Beginning, which fly yieldi dry beast moved blessed</p>
</div>
<div class="card" style="left:491px;top:1222px;height:302px">
  <div class="pic" style="background:linear-gradient(120deg,#2f6a6a 0%,#8a93a8 45%,#b9bcc8 70%,#5a6584)" role="img" aria-label="Small bedroom with teal curtains, desk and window"></div>
  <p style="padding-top:20px">Beginning fourth dominion creeping god was. Beginning, which fly yieldi dry beast moved blessed</p>
</div>
<div class="card" style="left:728px;top:1222px;height:291px">
  <div class="pic" style="background:linear-gradient(160deg,#5c5a5c 0%,#8d8a86 40%,#d5d6dc 70%,#3a4a8a)" role="img" aria-label="Hotel bedroom with upholstered headboard wall and patterned bedding"></div>
  <p>Beginning fourth dominion creeping god was. Beginning, which fly yieldi dry beast moved blessed</p>
</div>

<!-- video band -->
<section class="frame band" role="img" aria-label="Bedroom with tufted grey bedspread, black armchair and dark wooden dresser"></section>
<div class="abs play"><svg width="12" height="12" viewBox="0 0 12 12"><path d="M3 1l8 5-8 5z" fill="#c9a46c"/></svg></div>
<div class="abs band-title">Merrivale</div>
<div class="abs band-sub">View four has said does men saw find dear shy talent</div>

<!-- facilities -->
<section class="frame facilities"></section>
<svg class="abs sec-icon" style="top:2040px" height="22" viewBox="0 0 44 22"><path d="M4 9h36v8H4zM8 9V3h28v6M6 17v4M38 17v4" fill="none" stroke="#c9a46c" stroke-width="1.6"/></svg>
<h2 class="abs sec-title" style="top:2069px">Special Facilities</h2>

<div class="fac" style="left:253px">
  <h3><svg width="13" height="12" viewBox="0 0 13 12"><path d="M1 6l5.5-5L12 6M2.5 5v6h8V5" fill="none" stroke="#c9a46c" stroke-width="1.2"/></svg>Conference Room</h3>
  <p>Built purse maids cease her ham new seven among and. Pulled coming wooded tended it answer remain</p>
</div>
<div class="fac" style="left:491px">
  <h3><svg width="12" height="12" viewBox="0 0 12 12"><path d="M2 9h8L9 7V5a3 3 0 00-6 0v2zM5 11h2" fill="none" stroke="#c9a46c" stroke-width="1.2"/></svg>Swimming Pool</h3>
  <p>Built purse maids cease her ham new seven among and. Pulled coming wooded tended it answer remain</p>
</div>
<div class="fac" style="left:728px">
  <h3><svg width="15" height="11" viewBox="0 0 15 11"><path d="M1 8V5l2-3h9l2 3v3zM1 5h13" fill="none" stroke="#c9a46c" stroke-width="1.2"/><circle cx="4" cy="9" r="1.3" fill="#c9a46c"/><circle cx="11" cy="9" r="1.3" fill="#c9a46c"/></svg>Sports Culb</h3>
  <p>Built purse maids cease her ham new seven among and. Pulled coming wooded tended it answer remain</p>
</div>

<!-- testimonials -->
<svg class="abs sec-icon" style="top:2469px" height="22" viewBox="0 0 44 22"><path d="M4 9h36v8H4zM8 9V3h28v6M6 17v4M38 17v4" fill="none" stroke="#c9a46c" stroke-width="1.6"/></svg>
<h2 class="abs sec-title" style="top:2498px">Our Guest Love Us</h2>

<div class="abs quote-track">
  <div class="quote" style="left:-51px">
    <span class="avatar" role="img" aria-label="Guest portrait"></span>
    <div><p>Incidunt deleniti blanditiis quas aperiam recusandae consillo ullam quibusdam cum libero illo repell endus!</p><h4>Dana Holt</h4><span>CEO &amp; Founder</span></div>
  </div>
  <div class="quote" style="left:187px">
    <span class="avatar" role="img" aria-label="Guest portrait"></span>
    <div><p>Incidunt deleniti blanditiis quas aperiam recusandae consillo ullam quibusdam cum libero illo repell endus!</p><h4>Aaron Price</h4><span>CEO &amp; Founder</span></div>
  </div>
  <div class="quote" style="left:424px">
    <span class="avatar" role="img" aria-label="Guest portrait"></span>
    <div><p>Incidunt deleniti blanditiis quas aperiam recusandae consillo ullam quibusdam cum libero illo repell endus!</p><h4>Robin Marsh</h4><span>CEO &amp; Founder</span></div>
  </div>
  <div class="quote" style="left:661px">
    <span class="avatar" role="img" aria-label="Guest portrait"></span>
    <div><p>Incidunt deleniti blanditiis quas aperiam recusandae.</p></div>
  </div>
</div>
<div class="abs dots"><i class="on"></i><i></i><i></i></div>

<!-- news -->
<svg class="abs sec-icon" style="top:2867px" height="22" viewBox="0 0 44 22"><path d="M4 9h36v8H4zM8 9V3h28v6M6 17v4M38 17v4" fill="none" stroke="#c9a46c" stroke-width="1.6"/></svg>
<h2 class="abs sec-title" style="top:2896px">News &amp; Events</h2>

<article class="card news" style="left:253px;top:2983px;height:372px">
  <div class="pic" style="background:linear-gradient(180deg,#9aa8bc 0%,#8d6a4f 40%,#4f7e99 75%,#7aa6bd)" role="img" aria-label="Bedroom with carved headboard and blue quilt"></div>
  <h3>Lorem Ipsum</h3>
  <div class="meta"><span><b>▭</b> 20th Nov, 2018</span><span><b>▭</b> 03 Comments</span></div>
  <p>Not thoughts all exercise blessing Indulgence way everything joy alteration boisterous the attachment party we years to order</p>
</article>
<article class="card news" style="left:491px;top:2983px;height:372px">
  <div class="pic" style="background:linear-gradient(120deg,#2f6a6a 0%,#8a93a8 45%,#b9bcc8 70%,#5a6584)" role="img" aria-label="Small bedroom with teal curtains and desk"></div>
  <h3>Lorem Ipsum</h3>
  <div class="meta"><span><b>▭</b> 20th Nov, 2018</span><span><b>▭</b> 03 Comments</span></div>
  <p>Not thoughts all exercise blessing Indulgence way everything joy alteration boisterous the attachment party we years to order</p>
</article>
<article class="card news" style="left:728px;top:2983px;height:372px">
  <div class="pic" style="background:linear-gradient(160deg,#5c5a5c 0%,#8d8a86 40%,#d5d6dc 70%,#3a4a8a)" role="img" aria-label="Hotel bedroom with patterned bedding"></div>
  <h3>Lorem Ipsum</h3>
  <div class="meta"><span><b>▭</b> 20th Nov, 2018</span><span><b>▭</b> 03 Comments</span></div>
  <p>Not thoughts all exercise blessing Indulgence way everything joy alteration boisterous the attachment party we years to order</p>
</article>

<!-- footer -->
<footer class="frame footer"></footer>
<div class="fcol" style="left:253px"><h5>Top Products</h5><a>Managed Website</a><a>Manage Reputation</a><a>Power Tools</a><a>Marketing Service</a></div>
<div class="fcol" style="left:372px"><h5>Quick Links</h5><a>Jobs</a><a>Brand Assets</a><a>Investor Relations</a><a>Terms of Service</a></div>
<div class="fcol" style="left:491px"><h5>Features</h5><a>Jobs</a><a>Brand Assets</a><a>Investor Relations</a><a>Terms of Service</a></div>
<div class="fcol" style="left:609px"><h5>Resources</h5><a>Guides</a><a>Research</a><a>Experts</a><a>Agencies</a></div>
<div class="fcol" style="left:728px"><h5>Newsletter</h5><div class="note">You can trust us. we only send promo offers,</div>
  <div class="sub"><span class="field">Your Email Address</span><span class="go">Subscribe</span></div>
</div>
<div class="abs copy">Copyright ©2020 All rights reserved | This template is made with ♥ by <em>Larkfield Studio</em></div>
<div class="abs fsocial"><i></i><i></i><i></i><i></i></div>

</body>
</html>
```